24 Hour Fitness Center Store front. Window advertisment

We need a signage design for a 24 hour fitness center in Central FL. Bright Peak Fitness. I have attached photos that show our store front. The signage will cover 4 windows from the far left side towards the right, and 3 windows from the far right towards the left. So 7 windows total. The middle windows including the doors will be blank for customers to see inside.
We want to portray "Results" when people walk up. Our colors are shown on our Logo (attached). Red, gray, black. We are open to any ideas and concepts as far as how the layout is shown, example: Each window a different image, or one large image on each side shown through all windows. I have also attached some examples of other stores that look appealing. Our Services include 24 hour access, personal training, tanning, and group exercise. Each window is approximately 60 inches wide and 75 inches tall.
Thank you!
Fitness

```html
<!DOCTYPE html>
<html lang="en">
<head>
<meta charset="utf-8">
<title>Bright Peak Fitness – Window Panel S</title>
<link rel="stylesheet" href="https://fonts.googleapis.com/css2?family=Anton&display=swap">
<style>
  :root {
    --brand-red: #ec4034;
    --photo-dark: #1c1c1e;
    --photo-mid: #4a4a4e;
    --photo-light: #b9a393;
    --mark-charcoal: #2a2a2c;
  }
  html, body {
    margin: 0;
    padding: 0;
    overflow: hidden;
  }
  .window-panel {
    position: relative;
    width: 960px;
    height: 1200px;
    background: var(--brand-red);
    overflow: hidden;
  }
  .letter-cutout {
    position: absolute;
    left: 0;
    top: 0;
    width: 960px;
    height: 1200px;
  }
  .letter-cutout text {
    font-family: "Anton", "Impact", sans-serif;
  }
  .brand-signature {
    position: absolute;
    left: 44px;
    top: 1090px;
    display: flex;
    align-items: center;
    gap: 12px;
  }
  .brand-dot {
    width: 30px;
    height: 30px;
    border-radius: 50%;
    background: var(--mark-charcoal);
  }
  .brand-name {
    font-family: "Anton", "Impact", sans-serif;
    font-size: 28px;
    letter-spacing: 1px;
    text-transform: uppercase;
    color: var(--mark-charcoal);
    line-height: 1;
  }
</style>
</head>
<body>
  <main class="window-panel">
    <svg class="letter-cutout" viewBox="0 0 960 1200" role="img"
         aria-label="Large letter S filled with a photo of a muscular athlete seated on a shoulder press machine in a dark gym">
      <defs>
        <radialGradient id="athlete-photo-tones" cx="50%" cy="50%" r="55%">
          <stop offset="0%" stop-color="var(--photo-light)"/>
          <stop offset="45%" stop-color="var(--photo-mid)"/>
          <stop offset="100%" stop-color="var(--photo-dark)"/>
        </radialGradient>
      </defs>
      <text x="232" y="1037" font-size="1033" textLength="502"
            lengthAdjust="spacingAndGlyphs" fill="url(#athlete-photo-tones)">S</text>
    </svg>

    <div class="brand-signature">
      <span class="brand-dot"></span>
      <span class="brand-name">Bright Peak Fitness</span>
    </div>
  </main>
</body>
</html>
```